Cleaners Needs Bounce-Back Coupon For Laundry Service

We need a "bounce-back" coupon to attach to peoples dry cleaning orders that offers one free wash-n-fold laundry service. Right now we always attach their receipt to the bag that contains their dry cleaning when we return it. We'd like to also attach a coupon that will entice them to come try our laundry service.

Background on the service: We sort, wash, dry, and fold the laundry for customers and then neatly put it in a nice bag that makes returning very convenient. Their laundry comes out fresh, clean, smelling great, and without the hassle of doing it themselves. We have a great return rate. Most customers that try out the service become long term customers. The goal is to get our dry cleaning customers to come try it out.

Requirements:
* 5" x 8" and one-sided.
* To be printed on a standard color of card stock.
* Must incorporate our logo.
* Needs a place for us to fill in an expiration date. We'll fill in a date about two weeks out from the time they pick up their dry cleaning.
* Limit one coupon per customer.
* Limit 50 pounds of laundry per coupon.

```html
<!DOCTYPE html>
<html lang="en">
<head>
<meta charset="utf-8">
<title>Suds Lane Laundry – Bounce-Back Coupon</title>
<link rel="stylesheet" href="https://fonts.googleapis.com/css2?family=Bebas+Neue&family=Lato:wght@400;700&display=swap">
<style>
  :root {
    --page: #ffffff;
    --card-top: #e4eff9;
    --card-mid: #eef5fc;
    --cloud: #ffffff;
    --brand-blue: #1b3fa8;
    --logo-blue: #2f6fd6;
    --accent-orange: #f2640f;
    --bubble-edge: #8cc3ea;
    --bubble-fill: #d8ecfa;
    --price-blue: #1d62b0;
    --ink: #1e1e1e;
    --ink-soft: #444444;
  }
  * { margin: 0; padding: 0; box-sizing: border-box; }
  html, body { width: 1200px; height: 900px; overflow: hidden; background: var(--page); }
  .stage { position: relative; width: 1200px; height: 900px; }
  .coupon {
    position: absolute; left: 316px; top: 0; width: 568px; height: 900px;
    background: linear-gradient(180deg, var(--card-top) 0%, var(--card-mid) 60%, var(--card-top) 100%);
    overflow: hidden;
  }
  .coupon-art { position: absolute; inset: 0; }
  .brand {
    position: absolute; left: 58px; top: 86px;
    display: flex; align-items: center; gap: 16px;
  }
  .brand-square { width: 74px; height: 74px; background: var(--logo-blue); border-radius: 6px; }
  .brand-name {
    font-family: "Bebas Neue", sans-serif; font-size: 52px; line-height: 1;
    color: var(--logo-blue); letter-spacing: 1px;
  }
  .service-badge {
    position: absolute; border-radius: 50%;
    background: var(--accent-orange); border: 4px solid #fff;
    display: flex; align-items: center; justify-content: center;
    font-family: "Bebas Neue", sans-serif; color: #fff;
  }
  .badge-wash { left: 34px; top: 383px; width: 70px; height: 70px; font-size: 26px; }
  .badge-fold { left: 253px; top: 338px; width: 80px; height: 80px; font-size: 30px; }
  .badge-dry  { left: 484px; top: 258px; width: 70px; height: 70px; font-size: 26px; }
  .about-title {
    position: absolute; left: 0; width: 568px; top: 478px; text-align: center;
    font-family: "Bebas Neue", sans-serif; font-size: 42px; color: var(--brand-blue);
    letter-spacing: 0.5px;
  }
  .about-body {
    position: absolute; left: 40px; width: 488px; top: 528px; text-align: center;
    font-family: "Lato", sans-serif; font-size: 17px; line-height: 27px; color: var(--ink);
  }
  .offer-value {
    position: absolute; left: 436px; top: 660px; width: 96px; height: 96px;
    display: flex; align-items: center; justify-content: center;
    font-family: "Bebas Neue", sans-serif; font-size: 46px; color: var(--price-blue);
  }
  .expiry {
    position: absolute; left: 36px; top: 768px;
    font-family: "Lato", sans-serif; font-weight: 700; font-size: 16px; color: var(--ink-soft);
    display: flex; align-items: flex-end;
  }
  .expiry-line { display: inline-block; width: 100px; border-bottom: 1.5px solid var(--ink-soft); margin-left: 4px; height: 16px; }
  .terms {
    position: absolute; left: 36px; top: 825px; list-style: none;
    font-family: "Lato", sans-serif; font-size: 17px; line-height: 27px; color: #333;
  }
</style>
</head>
<body>
<div class="stage">
  <section class="coupon">
    <svg class="coupon-art" width="568" height="900" viewBox="0 0 568 900">
      <defs>
        <radialGradient id="bubble" cx="40%" cy="35%" r="65%">
          <stop offset="0" stop-color="#ffffff"/>
          <stop offset="0.7" stop-color="var(--bubble-fill)"/>
          <stop offset="1" stop-color="var(--bubble-edge)"/>
        </radialGradient>
        <linearGradient id="washTone" x1="0" y1="0" x2="1" y2="1">
          <stop offset="0" stop-color="#e9ecef"/><stop offset="1" stop-color="#9fb4c4"/>
        </linearGradient>
        <linearGradient id="foldTone" x1="0" y1="0" x2="0" y2="1">
          <stop offset="0" stop-color="#b8523a"/><stop offset="0.45" stop-color="#e3d27a"/><stop offset="1" stop-color="#d9c863"/>
        </linearGradient>
        <linearGradient id="dryTone" x1="0" y1="0" x2="1" y2="1">
          <stop offset="0" stop-color="#eef0f2"/><stop offset="1" stop-color="#b3474a"/>
        </linearGradient>
      </defs>

      <!-- decorative bubbles -->
      <g fill="url(#bubble)" stroke="var(--bubble-edge)" stroke-width="1">
        <circle cx="90" cy="24" r="8"/><circle cx="116" cy="33" r="12"/><circle cx="94" cy="48" r="6"/>
        <circle cx="463" cy="77" r="42"/><circle cx="505" cy="132" r="20"/><circle cx="462" cy="150" r="13"/>
        <circle cx="490" cy="172" r="10"/><circle cx="516" cy="163" r="6"/><circle cx="524" cy="182" r="5"/>
        <circle cx="292" cy="445" r="30" opacity="0.5"/><circle cx="220" cy="425" r="20" opacity="0.4"/>
        <circle cx="437" cy="766" r="13"/><circle cx="476" cy="785" r="19"/><circle cx="440" cy="800" r="9"/>
        <circle cx="462" cy="815" r="6"/><circle cx="456" cy="830" r="5"/>
      </g>

      <!-- service photo areas -->
      <circle cx="139" cy="345" r="95" fill="url(#washTone)" stroke="#fff" stroke-width="3" role="img" aria-label="Photo of laundry spilling from a front-loading washing machine"/>
      <circle cx="449" cy="345" r="90" fill="url(#dryTone)" stroke="#fff" stroke-width="3" role="img" aria-label="Photo of clothes inside a tumble dryer drum"/>
      <circle cx="294" cy="283" r="88" fill="url(#foldTone)" stroke="#fff" stroke-width="3" role="img" aria-label="Photo of a stack of neatly folded towels"/>

      <!-- clouds -->
      <g fill="var(--cloud)">
        <ellipse cx="80" cy="700" rx="140" ry="75"/>
        <ellipse cx="230" cy="720" rx="130" ry="70"/>
        <ellipse cx="380" cy="735" rx="110" ry="60"/>
        <ellipse cx="540" cy="700" rx="90" ry="60"/>
        <rect x="0" y="740" width="568" height="160"/>
      </g>

      <!-- price bubble -->
      <circle cx="484" cy="707" r="48" fill="url(#bubble)" stroke="var(--bubble-edge)" stroke-width="2"/>
    </svg>

    <header class="brand">
      <span class="brand-square"></span>
      <span class="brand-name">Suds Lane Laundry</span>
    </header>

    <span class="service-badge badge-wash">Wash</span>
    <span class="service-badge badge-fold">Fold</span>
    <span class="service-badge badge-dry">Dry</span>

    <h1 class="about-title">About Suds Lane Laundry</h1>
    <p class="about-body">Right now we always attach their receipt to the bag that contains their dry cleaning when we return it. We'd like to also attach a coupon that will entice them to come try our laundry service.</p>

    <div class="offer-value">£50</div>

    <p class="expiry">Expire Date:<span class="expiry-line"></span></p>
    <ul class="terms">
      <li>* LIMIT ONE COUPON PER CUSTOMER.</li>
      <li>* LIMIT 50 POUNDS OF LAUNDRY PER COUPON.</li>
    </ul>
  </section>
</div>
</body>
</html>
```